Oven Cleaning flyer design

Hi there,
I need help designing a letterbox flyer. It needs to be DL size.
I have attached a rough design made with Chat GPT.
Would like back and front, have my business colors.
Please find attached mock up of what I would roughly like.
Also find attached logo.
Thank you

Target Market(s)

Home owners over 40

Industry/Entity Type

Cleaning

Requirements
Must have
• Logo, before after of oven, brand colors

```html
<!DOCTYPE html>
<html lang="en">
<head>
<meta charset="utf-8">
<title>Hearthbright – DL Flyer Front and Back</title>
<link rel="stylesheet" href="https://fonts.googleapis.com/css2?family=Red+Hat+Display:ital,wght@0,400;0,500;0,700;0,800;1,800&display=swap">
<style>
  :root {
    --teal: #47c1c9;
    --ink: #111111;
    --paper: #ffffff;
    --backdrop: #e4e4e4;
    --before-a: #6b5a44;
    --before-b: #a8773c;
    --after-a: #9aa2a6;
    --after-b: #dfe3e5;
  }
  * { margin: 0; padding: 0; box-sizing: border-box; }
  html, body { width: 944px; height: 1200px; overflow: hidden; }
  body {
    background: var(--backdrop);
    font-family: "Red Hat Display", Arial, sans-serif;
    color: var(--ink);
    position: relative;
  }
  .flyer {
    position: absolute;
    top: 185px;
    width: 394px;
    height: 848px;
    background: var(--paper);
    overflow: hidden;
  }
  .flyer--front { left: 60px; }
  .flyer--back { left: 489px; }
  .flyer__shapes { position: absolute; inset: 0; width: 100%; height: 100%; }
  .flyer > *:not(.flyer__shapes) { position: absolute; left: 0; right: 0; text-align: center; }

  .brand {
    top: 48px;
    display: flex;
    align-items: center;
    justify-content: center;
    gap: 14px;
  }
  .brand__dot { width: 52px; height: 52px; border-radius: 50%; background: var(--teal); }
  .brand__name {
    font-weight: 800;
    font-size: 30px;
    letter-spacing: 1px;
    color: var(--teal);
  }

  .headline { font-weight: 700; font-size: 32px; line-height: 42px; }
  .headline--light { color: var(--paper); top: 218px; }
  .headline--dark { color: var(--ink); top: 194px; }

  .intro { font-size: 13.4px; line-height: 18px; padding: 0 40px; }
  .intro--light { color: var(--paper); top: 318px; }
  .intro--dark { color: var(--ink); top: 305px; padding: 0 32px; }

  .proof { top: 395px; left: 49px !important; right: auto !important; width: 302px; height: 300px; background: var(--teal); }
  .proof__frame { position: absolute; left: 11px; top: 20px; width: 280px; height: 230px; background: var(--paper); display: flex; gap: 2px; padding: 8px 9px; }
  .proof__photo { flex: 1; }
  .proof__photo--before { background: linear-gradient(180deg, var(--before-a), var(--before-b)); }
  .proof__photo--after { background: linear-gradient(180deg, var(--after-a), var(--after-b)); }
  .proof__labels { position: absolute; left: 0; right: 0; top: 265px; display: flex; }
  .proof__label { flex: 1; text-align: center; font-style: italic; font-weight: 800; font-size: 15px; color: var(--ink); }

  .call { top: 720px; font-size: 13.5px; line-height: 18px; }
  .phone { font-size: 21px; }
  .flyer--front .phone { top: 773px; }
  .web-band { top: 805px; height: 23px; background: var(--teal); color: var(--paper); font-size: 13px; line-height: 23px; letter-spacing: 2.4px; }

  .offer { top: 554px; color: var(--paper); font-size: 19px; line-height: 26px; }
  .offer strong { font-weight: 700; }
  .perks { top: 638px; color: var(--paper); font-size: 13px; line-height: 17px; list-style: none; }
  .contact { top: 718px; color: var(--paper); font-size: 20px; line-height: 28px; }
  .extras { top: 794px; color: var(--paper); font-size: 13px; }
</style>
</head>
<body>

<section class="flyer flyer--front" aria-label="Flyer front">
  <svg class="flyer__shapes" viewBox="0 0 394 848" preserveAspectRatio="none" aria-hidden="true">
    <path d="M0 196 C110 160 260 148 394 150 L394 158 C250 158 110 175 0 210 Z" fill="var(--ink)"/>
    <path d="M0 205 C120 170 270 158 394 160 L394 470 C300 500 160 540 0 560 Z" fill="var(--teal)"/>
    <path d="M0 560 C160 540 300 500 394 470 L394 500 C300 530 160 575 0 595 Z" fill="var(--ink)"/>
  </svg>

  <div class="brand">
    <span class="brand__dot"></span>
    <span class="brand__name">HEARTHBRIGHT</span>
  </div>

  <h1 class="headline headline--light">Bring Your Oven<br>Back to Life</h1>
  <p class="intro intro--light">Professional, non-caustic oven cleaning that removes built-up grease, smoke, and burnt grime - leaving your oven looking fresh again.</p>

  <div class="proof">
    <div class="proof__frame">
      <div class="proof__photo proof__photo--before" role="img" aria-label="Photo of a dirty oven interior with burnt grease on the door"></div>
      <div class="proof__photo proof__photo--after" role="img" aria-label="Photo of the same oven after cleaning, with a clear glass door"></div>
    </div>
    <div class="proof__labels">
      <span class="proof__label">BEFORE</span>
      <span class="proof__label">AFTER</span>
    </div>
  </div>

  <p class="call">Call Now for<br>Fast, Professional Service</p>
  <p class="phone">0400 528 193</p>
  <p class="web-band">hearthbright.com.au</p>
</section>

<section class="flyer flyer--back" aria-label="Flyer back">
  <svg class="flyer__shapes" viewBox="0 0 394 848" preserveAspectRatio="none" aria-hidden="true">
    <path d="M0 560 C110 480 250 440 394 432 L394 440 C250 450 110 500 0 590 Z" fill="var(--ink)"/>
    <path d="M0 590 C110 500 250 450 394 440 L394 848 L70 848 C40 800 15 750 0 700 Z" fill="var(--teal)"/>
    <path d="M0 700 C15 750 40 800 70 848 L50 848 C30 805 12 760 0 725 Z" fill="var(--ink)"/>
  </svg>

  <div class="brand">
    <span class="brand__dot"></span>
    <span class="brand__name">HEARTHBRIGHT</span>
  </div>

  <h2 class="headline headline--dark">Why Choose<br>Hearthbright?</h2>
  <p class="intro intro--dark">We're a local family business providing professional, non-caustic oven cleaning across Sunshine Coast. Using specialized-equipment and proven cleaning methods, equipment and proven cleaning methods, we remove heavy grease, carbon build-up, smoke residue, restoring your oven safely and effectively.</p>

  <p class="offer">Mention this flyer for<br><strong>$10 off</strong> your first clean</p>
  <ul class="perks">
    <li>Reliable Service</li>
    <li>Non-Caustic Cleaning</li>
    <li>Satisfaction Guaranteed</li>
  </ul>
  <p class="contact">0400 528 193<br>hearthbright.com.au</p>
  <p class="extras">We also clean cooktops, rangehoods and BBQs</p>
</section>

</body>
</html>
```